Quorvin Upcoming Gigs

One page graphic with my upcoming dates. Logo and photo attached, and sample from last flyer. Text:

QUORVIN

UPCOMING DATES

3/26/18 Tidal Plums (Las Vegas, NV)

4/1/18 Venture Hollow 2847 M St (Sac, CA)

4/8/18 Amber Heron (Sac, CA)

5/5/18 Low Ceiling @ Silver Moth (Sac, CA)

5/10/18 Pellman Art Museum (Sac, CA)

5/11/18 Vif Brume @ Cafe du Lierre (Sac, CA)

5/27/18 Sonnlicht JTR @ Vox (Sac, CA)

Save The Date: 9/21/18 Lanterns Festival (Puerto Nuevo, MX)

plazabook.example/quorvin482

Target Market(s)

House/Electronic Music

Industry/Entity Type

Night Club

Font styles to use
Sans Serif

Colors

Designer to choose colors to be used in the design.

Requirements
Must have
• Quorvin logo or something that looks good instead. Prefer photo to be in but not necessary.
Nice to have

```html
<!DOCTYPE html>
<html lang="en">
<head>
<meta charset="utf-8">
<title>Quorvin Upcoming Dates</title>
<link rel="stylesheet" href="https://fonts.googleapis.com/css2?family=Montserrat:wght@200;400;800&display=swap">
<style>
  :root {
    --stage: #e9e6e3;
    --flyer-black: #070609;
    --ink: #f4f2f6;
    --ink-soft: #cfcad6;
    --glow-violet: #5a2ca8;
    --glow-magenta: #a8287a;
    --deck-warm: #d8a07a;
    --deck-blue: #2a3a8a;
    --deck-red: #c8303a;
  }
  * { box-sizing: border-box; margin: 0; padding: 0; }
  html, body {
    width: 1200px; height: 675px; overflow: hidden;
    background: var(--stage);
    font-family: "Montserrat", sans-serif;
  }
  .canvas {
    position: relative; width: 1200px; height: 675px;
    display: flex; align-items: center; justify-content: center; gap: 60px;
  }
  .flyer {
    position: relative; width: 420px; height: 594px;
    background: var(--flyer-black);
    overflow: hidden;
    box-shadow: 0 6px 22px rgba(0,0,0,.25);
    color: var(--ink);
  }

  /* Back side: gig list */
  .back__photo {
    position: absolute; left: 0; right: 0; bottom: 0; height: 330px;
    background:
      radial-gradient(ellipse 100px 80px at 62% 42%, rgba(216,160,122,.55), transparent 70%),
      radial-gradient(ellipse 190px 110px at 70% 75%, rgba(168,40,122,.55), transparent 75%),
      radial-gradient(ellipse 210px 180px at 55% 35%, rgba(90,44,168,.75), transparent 75%);
  }
  .back__brand {
    position: absolute; left: 22px; top: 420px;
    transform: rotate(-90deg); transform-origin: left top;
    font-weight: 800; font-size: 66px; letter-spacing: 2px;
    line-height: 1; white-space: nowrap;
  }
  .back__heading { position: absolute; left: 102px; top: 52px; }
  .heading__upcoming {
    display: block; font-weight: 200; font-size: 42px; letter-spacing: 1px; line-height: 1;
  }
  .heading__dates {
    display: block; font-weight: 800; font-size: 34px; letter-spacing: 1px; line-height: 1;
  }
  .gig-list {
    position: absolute; left: 102px; top: 140px; list-style: none;
    font-size: 11.5px; line-height: 25px; white-space: nowrap;
  }
  .gig__date { font-weight: 400; }
  .gig__venue { font-weight: 800; }
  .gig__place { font-weight: 400; font-size: 9.5px; color: var(--ink-soft); }

  /* Front side: cover */
  .front__photo {
    position: absolute; left: 0; right: 0; top: 250px; bottom: 0;
    background:
      radial-gradient(ellipse 60px 22px at 30% 28%, rgba(200,48,58,.55), transparent 70%),
      radial-gradient(ellipse 70px 24px at 75% 8%, rgba(200,48,58,.45), transparent 70%),
      radial-gradient(ellipse 140px 70px at 50% 30%, rgba(42,58,138,.6), transparent 75%),
      radial-gradient(ellipse 260px 180px at 50% 45%, rgba(90,44,168,.55), transparent 75%),
      linear-gradient(180deg, rgba(7,6,9,0) 0%, rgba(30,20,60,.6) 60%, rgba(40,30,90,.5) 100%);
  }
  .front__title {
    position: absolute; left: 0; right: 0; top: 96px; text-align: center;
  }
  .front__brand {
    display: block; font-weight: 800; font-size: 70px; letter-spacing: 3px; line-height: 1;
  }
  .front__sub {
    position: absolute; right: 48px; top: 176px; text-align: right;
  }
  .front__sub .heading__upcoming { font-size: 36px; }
  .front__sub .heading__dates { font-size: 30px; }
  .front__link {
    position: absolute; left: 0; right: 0; bottom: 34px;
    display: flex; flex-direction: column; align-items: center; gap: 6px;
    font-size: 10px; font-weight: 400; color: var(--ink-soft);
  }
  .front__dot {
    width: 16px; height: 16px; border-radius: 50%; background: var(--ink);
  }
</style>
</head>
<body>
<main class="canvas">
  <article class="flyer flyer--back">
    <div class="back__photo" role="img" aria-label="DJ performing at the decks against a brick wall lit in purple"></div>
    <h1 class="back__brand">QUORVIN</h1>
    <h2 class="back__heading">
      <span class="heading__upcoming">UPCOMING</span>
      <span class="heading__dates">DATES</span>
    </h2>
    <ul class="gig-list">
      <li><span class="gig__date">3/26/18</span> <span class="gig__venue">Tidal Plums</span> <span class="gig__place">(Las Vegas, NV)</span></li>
      <li><span class="gig__date">4/1/18</span> <span class="gig__venue">Venture Hollow 2847 M St</span> <span class="gig__place">(Sac, CA)</span></li>
      <li><span class="gig__date">4/8/18</span> <span class="gig__venue">Amber Heron</span> <span class="gig__place">(Sac, CA)</span></li>
      <li><span class="gig__date">5/5/18</span> <span class="gig__venue">Low Ceiling @ Silver Moth</span> <span class="gig__place">(Sac, CA)</span></li>
      <li><span class="gig__date">5/10/18</span> <span class="gig__venue">Pellman Art Museum</span> <span class="gig__place">(Sac, CA)</span></li>
      <li><span class="gig__date">5/11/18</span> <span class="gig__venue">Vif Brume @ Cafe du Lierre</span> <span class="gig__place">(Sac, CA)</span></li>
      <li><span class="gig__date">5/27/18</span> <span class="gig__venue">Sonnlicht JTR @ Vox</span> <span class="gig__place">(Sac, CA)</span></li>
      <li><span class="gig__venue">Save The Date:</span></li>
      <li><span class="gig__date">9/21/18</span> <span class="gig__venue">Lanterns Festival</span> <span class="gig__place">(Puerto Nuevo, MX)</span></li>
    </ul>
  </article>

  <article class="flyer flyer--front">
    <div class="front__photo" role="img" aria-label="Close view of a DJ controller with glowing pads and jog wheels"></div>
    <h1 class="front__title"><span class="front__brand">QUORVIN</span></h1>
    <h2 class="front__sub">
      <span class="heading__upcoming">UPCOMING</span>
      <span class="heading__dates">DATES</span>
    </h2>
    <p class="front__link"><span class="front__dot"></span><span>plazabook.example/quorvin482</span></p>
  </article>
</main>
</body>
</html>
```